Zielgruppe
Wir sind ein kleines Restaurant in den schweizer Bergen. Unsere sonnige Terrasse mit bester Aussicht auf die umliegende Berglandschaft, läd zum verweilen und geniessen ein. Unser Publikum sind vor allem mehr oder weniger sportliche Schweizer jeden Alters, die auf ihrem Weg zu/von den umliegenden Wanderungen bei uns vorbei kommen, aber auch ältere Semester die nicht mehr so gut zu Fuß sind und deshalb auf der Terrasse verweilen. Auch Touristen kommen vorbei, wir sind für die aber mehr ein Geheimtipp. Am späten Nachmittag kommen ein paar Anwohner vorbei auf ein Feierabendgetränk und am Wochenende haben wir öfters die selben 'Einheimischen' hier für ein Mittagessen. Unser Angebot ist eher traditionell gehalten, aber wir wollen Gerichte anbieten die nicht auf jeder Hütte zu finden sind. Ich komme aus Tirol, meine Mitarbeiterin hier aus der Schweiz - deshalb haben wir einen Mix aus beiden Nationen auf den Tellern. Wir streben einen moderneren/coolen Stil an, der zu uns 'jungen Mädels' passt, der aber noch stark von Tradition und der Bergwelt geprägt ist. Unser Stübli ist sehr urig, aus dunkelm Holz gebaut und mit weissen Schaffellen und Kissen gemütlich gemacht. Die Einrichtung haben wir in den Farben weiss, dunkelrot und beige-brauntönen gehalten.
Aufgabenstellung
bitte nichts kitschiges oder zu buntes.
Die Masse 25x25 oder 26x26 gefallen uns am besten.
Der 'Hinweis' mit der MwSt und CHF sowie Kartenzahlung sollte bitte als kleine Fusszeile auf jeder Seite (ausser Titelseite und zweite Seite) sein

```html
<!DOCTYPE html>
<html lang="de">
<head>
<meta charset="utf-8">
<title>Felsegg Stübli – Speisekarte</title>
<link href="https://fonts.googleapis.com/css2?family=Kaushan+Script&family=Zilla+Slab:ital,wght@0,400;0,600;1,400&display=swap" rel="stylesheet">
<style>
  :root {
    --backdrop: #e3e0d2;
    --panel: #ebe1d8;
    --ink: #37322f;
    --ink-soft: #4a4340;
    --accent: #b5804c;
    --wood: #3d3a37;
    --wood-dark: #2b2927;
    --sky-top: #6f9ad6;
    --sky-mid: #bcd0e6;
    --valley: #4d5a3a;
    --white: #ffffff;
  }
  * { box-sizing: border-box; margin: 0; padding: 0; }
  html, body {
    width: 1200px; height: 884px; overflow: hidden;
    background: var(--backdrop);
  }
  .spread {
    position: absolute; left: 136px; top: 203px;
    width: 926px; height: 465px;
    display: flex;
  }
  .page { position: relative; width: 463px; height: 465px; overflow: hidden; }

  /* left page */
  .landscape {
    position: absolute; inset: 0;
    background:
      linear-gradient(180deg, var(--sky-top) 0%, #9cbbe0 18%, var(--sky-mid) 30%, #9aa0a2 42%, #6a6a58 58%, var(--valley) 78%, #6b7a3a 100%);
  }
  .welcome {
    position: absolute; left: 86px; top: 41px; width: 292px; height: 384px;
    background: linear-gradient(180deg, rgba(235,225,216,0.12) 0%, rgba(235,225,216,0.55) 30%, var(--panel) 52%, var(--panel) 100%);
    text-align: center;
    color: var(--ink);
    font-family: "Zilla Slab", serif;
  }
  .welcome__title {
    margin-top: 14px;
    font-family: "Kaushan Script", cursive;
    color: var(--white);
    font-size: 19px; line-height: 20px; font-weight: 400;
  }
  .welcome__name {
    margin-top: 40px;
    font-size: 25px; color: var(--ink); font-weight: 400;
  }
  .welcome__rule {
    width: 145px; height: 1px; background: var(--ink);
    margin: 6px auto 0;
  }
  .welcome__altitude {
    margin-top: 7px; font-size: 8px; font-style: italic; letter-spacing: 0.5px;
  }
  .welcome__text {
    margin-top: 30px; font-size: 8.4px; line-height: 10.6px; font-style: italic;
    color: var(--ink-soft);
  }
  .welcome__text p + p { margin-top: 10px; }
  .footnote {
    position: absolute; left: 0; right: 0; bottom: 17px;
    font-size: 6.4px; line-height: 8px; color: var(--ink-soft);
  }

  /* right page */
  .wood {
    position: absolute; inset: 0;
    background: linear-gradient(90deg, var(--wood-dark) 0%, var(--wood) 20%, #46423e 45%, var(--wood) 75%, var(--wood-dark) 100%);
  }
  .section-title {
    position: absolute; left: 51px; top: 232px;
    transform: translate(-50%, -50%) rotate(-90deg);
    white-space: nowrap;
    font-family: "Kaushan Script", cursive;
    color: var(--white); font-size: 38px;
  }
  .menu {
    position: absolute; left: 87px; top: 41px; width: 295px; height: 383px;
    background: var(--panel);
    text-align: center; color: var(--ink);
    font-family: "Zilla Slab", serif;
  }
  .menu__heading {
    margin-top: 22px;
    font-family: "Kaushan Script", cursive;
    color: var(--accent); font-size: 18px; font-weight: 400; line-height: 20px;
  }
  .dish { margin-top: 7px; }
  .dish:first-of-type { margin-top: 9px; }
  .dish__name { font-size: 10px; font-weight: 600; line-height: 11px; }
  .dish__name span { font-weight: 400; }
  .dish__desc { font-size: 8px; font-style: italic; line-height: 10.5px; color: var(--ink-soft); }
  .dish__price { font-size: 8.5px; font-style: italic; font-weight: 600; color: var(--accent); line-height: 10.5px; }
  .bread-art {
    position: absolute; left: 102px; top: 316px; width: 90px; height: 44px;
    background: radial-gradient(ellipse at center, #dcc3a8 0%, rgba(235,225,216,0) 70%);
  }
</style>
</head>
<body>
  <main class="spread">
    <section class="page page--welcome">
      <div class="landscape" role="img" aria-label="Foto: Alpenpanorama mit verschneiten Gipfeln, Tal und herbstlichen Bäumen"></div>
      <div class="welcome">
        <h1 class="welcome__title">Ein herzliches Willkommen<br>im</h1>
        <div class="welcome__name">Felsegg Stübli</div>
        <div class="welcome__rule"></div>
        <div class="welcome__altitude">1520 m.ü.m</div>
        <div class="welcome__text">
          <p>Wir freuen uns, dass ihr da seid.<br>
          Hier im Felsegg Stübli könnt ihr entspannt durchatmen.<br>
          Lasst euch verwöhnen mit einheimischer und auch Tiroler Kost<br>
          aus frischen Zutaten. Entspannt Körper und Seele bei einem Glas<br>
          feinen Wein, wir bedienen euch gerne.</p>
          <p>Auf Felsegg gibt es weder Strom noch Kanalisation.<br>
          Bitte habt Verständnis mit uns, wenn nicht alles so schnell geht<br>
          wie in der Stadt – hier ticken die Uhren noch etwas anders.<br>
          Was im Tal selbstverständlich erscheint, erfordert hier<br>
          gute Planung und Handarbeit.</p>
          <p>Sprich uns gerne an und erfahre noch mehr über’s Felsegg<br>
          Stübli und wie wir hier so leben und arbeiten.</p>
        </div>
        <p class="footnote">Hinweis: alle Preise verstehen sich inkl. MwSt. und in CHF<br>
        Kartenzahlungen akzeptieren wir ab einem Mindestbetrag von 20,00</p>
      </div>
    </section>

    <section class="page page--menu">
      <div class="wood" role="img" aria-label="Hintergrund: dunkle, verwitterte Holzbretter"></div>
      <h2 class="section-title">Was hei mer z’Ässe?</h2>
      <div class="menu">
        <h3 class="menu__heading">Z’Nini</h3>
        <div class="dish">
          <div class="dish__name">Gipfeli,</div>
          <div class="dish__desc">frisch aus dem Ofen</div>
          <div class="dish__price">1,60</div>
        </div>
        <div class="dish">
          <div class="dish__name">Nussgipfel</div>
          <div class="dish__desc">mit viel Liebe von Hand gemacht</div>
          <div class="dish__price">5,00</div>
        </div>
        <div class="dish">
          <div class="dish__name">Stübli Sandwich</div>
          <div class="dish__desc">mit Salami und Hobelkäse von der Alp</div>
          <div class="dish__price">8,50</div>
        </div>
        <div class="dish">
          <div class="dish__name">Z’Vieriwurst mit Brot</div>
          <div class="dish__desc">geräucherte Wurst aus Rind und Schweinefleisch,<br>direkt vom Bauernhof</div>
          <div class="dish__price">12,50</div>
        </div>
        <div class="dish">
          <div class="dish__name">Portion Alpkäse <span>(100g)</span></div>
          <div class="dish__desc">von unseren Nachbars-Bauernhöfen in Felsegg<br>serviert mit Brot</div>
          <div class="dish__price">14,50</div>
        </div>
        <div class="dish">
          <div class="dish__name">Ein Paar Rauchwürste</div>
          <div class="dish__desc">Schweinswürste mit Raucharoma von unserem Metzger,<br>serviert mit Brot</div>
          <div class="dish__price">9,50</div>
        </div>
        <div class="bread-art" role="img" aria-label="Illustration: Brotlaib auf einem Schneidebrett mit Messer"></div>
      </div>
    </section>
  </main>
</body>
</html>
```